Greek Souvlaki Restaurant Menu Design

We would like to redesign our menu (at the moment just a price-list without any graphics) and create something more fun.

You can find all the items we are offering at the following link / our e-shop:
https://fennelandfig.example/orders/en/order/
I have also attached a printout of the above with hand written notes on the sections and items that will be included.

Our menu is divided to a couple of parts:
- Souvlaki Bar and Grill
- Authentic Greek Cuisine
- Wine List
- Desserts
- Bakaliko

This project will take on the first part of our menu, which is the Souvlaki Bar and Grill. If we are happy with your design, we will then develop the rest of our menu.

Souvlaki Bar and Grill
---------------------------

Our souvlaki can be customised to the customer requirements. The following links have similar set ups:

WOWZA!Bun
https://pinboard.example/pin/100000000000000001/
I like the way they have set it up, but the graphics and colours used are not my thing. I also like they way they have split up the steps, choose, top it of, etc.

The Crisp
https://pinboard.example/pin/100000000000000002/
I hate the step 1,2,3 on the left side. It does not make it playful. Like the fact that they have used pictures of the ingredients.

https://pinboard.example/pin/100000000000000003/
Hate the graphics, like the concept.

-------------

First Sections: Our Souvliaki Pita Wrap

The steps to customise a souvlaki can be found on the following link:
https://fennelandfig.example/orders/en/order/ and choose pita wrap.

Most of the one side of our Souvliaki/Grill menu should be dedicated to our Pita Wraps.

It should have a small description of the Greek Souvlaki Pita Wrap. Something along the lines of "Get a whole meal all wrapped up with our delicious Greek Pita Wraps. Containing protein, sauce and salad". Improvements of this line are welcome.

It should then have the steps to customise it.

Step One.
Choose Base:
1. Chicken Skewer
2. Pork Skewer
3. etc
Price and options can be found on the above link on our website

Step Two.
Add one of our delicious home made sauces.
Options can be found on our website.

Step Three
Finalise it with the ingredients of your choice.
The customer can select multiple incredients

Step Four.
Feeling Hungry? Add extras:
Extras and Prices can be found on the link provided.

Buy two wraps and save. Takeaway only!
You will find this option as "Double Souvlaki Pita Wrap Offer."
Instead of 2x5.5 = £11 pay £10.5. This offer should also be mentioned somewhere on this section.

-----

Second Section - Our Platters

Skewers Platter and Gyros Platter

Options can be found by clicking on the items on the link provided.

Extras and Pita Bread option are common. Meat options are different and skewers have a choice of side. Meat options have 2/3 skewers and 200/300 grams of gyros, so they can probably be combined somehow.

These section can also be called Naked / Open Souvlaki Platters

Third Section
From Our Grill

All options from this section together with modifiers (can be see if you click on each item). I would like pictures from each item.

Forth Section
Meal Deals, starter combo and Set Menu.

Meal Deal for 1/2 and 4 are wraps with extras. The for 4 is not on the pdf and will be up on our website soon, so please check. I think those are easy to e incorporated next to the pita wrap section as upgrades to save.

Set menus are various items.

If they can fit on this page somehow we incorporate them, if not we can make a separate page with the offers / meals deals. If a separate page is created them the meal deal from our kitchen and vegetarean set menu should also be included.

Fifth Section
Salads and Starter

I would like all options from Hot and Cold starter and our salad. I would like pictures next to all options, if possible.

-----

Final notes/ideas.

Wraps, platters and grill could be one page front and back. Salads and starters could be a different page(s) or sections.

The menu should be easily updated and we would like a format where we can update prices and descriptions.

Prices and descriptions can be found on the link provided.

Feel free to improve our descriptions and titles. Please do mention where you made improvements, so we can approve them.

Our kitchen, dessert and wine menu will be given as a separate project and priority will be given to the person that won this competition.

If you need better quality pictures please let us know, most of the pictures we do have them in raw format too.

------

Some designs that I like. To give you an idea of the design I would like to see:

https://www.craftstall.example/listing/200000001/american-menu-restaurant-cafe-menus
I would love to see something like that for the grill/salad/starter side of our menu, since it has space for pictures.

https://pinboard.example/pin/100000000000000004/
I would love to see something like that, where the incredients of a souvlaki come together. This is optional and does not have to be there.

https://pinboard.example/pin/100000000000000005/

https://pinboard.example/pin/100000000000000006/

https://pinboard.example/pin/100000000000000007/

https://pinboard.example/pin/100000000000000008/

Target Market(s)

London

Font styles to use
Serif
Sans Serif

Colors
abd037
3277b5
33a6d7

Requirements
Must have
• Build your own souvlaki section. See description for examples.

Pictures for starters and salads.

Should be elegant
Nice to have
• Incorporate our relevant meal deals on the souvlaki pita section

```html
<!DOCTYPE html>
<html lang="en">
<head>
<meta charset="utf-8">
<title>From Our Grill</title>
<link href="https://fonts.googleapis.com/css2?family=Kaushan+Script&family=Special+Elite&family=Montserrat:wght@400;600&display=swap" rel="stylesheet">
<style>
:root{
  --wood:#2b2b2b;
  --wood-light:#3a3a3a;
  --paper:#d9d5cf;
  --paper-light:#e6e3de;
  --ink:#2a2a2a;
  --ink-soft:#555;
  --rule:#6d6a66;
  --banner:#f4f3f1;
  --plate:#f2f1ee;
  --green:#abd037;
}
*{margin:0;padding:0;box-sizing:border-box}
html,body{width:777px;height:1200px;overflow:hidden;background:var(--wood)}
.menu-page{position:relative;width:777px;height:1200px;
  background:repeating-linear-gradient(90deg,var(--wood) 0 38px,var(--wood-light) 38px 40px,var(--wood) 40px 78px);
  font-family:"Montserrat",sans-serif;color:var(--ink)}
.paper-panel{position:absolute;left:0;top:0;width:440px;height:1160px;
  background:radial-gradient(ellipse at 40% 30%,var(--paper-light),var(--paper) 70%)}
.stitch-edge{position:absolute;left:3px;top:0;bottom:0;border-left:2px dotted #bbb}
.title-banner{position:absolute;left:32px;top:22px;width:745px;height:84px;background:var(--banner);
  clip-path:polygon(0 0,100% 0,100% 100%,0 100%,4% 50%)}
.title-banner::before,.title-banner::after{content:"";position:absolute;left:30px;right:0;border-top:2px dotted #999}
.title-banner::before{top:6px}.title-banner::after{bottom:6px}
.title-banner h1{position:absolute;left:160px;top:8px;font-family:"Kaushan Script",cursive;font-weight:400;font-size:52px;color:var(--ink);letter-spacing:1px}
.sprig{position:absolute;top:30px;width:115px;height:36px;background:linear-gradient(90deg,#cfcfcf,#9a9a9a)}
.sprig.left{left:40px}.sprig.right{left:512px;background:linear-gradient(90deg,#9a9a9a,#cfcfcf)}
.item-box{position:absolute;left:62px;width:360px;border:1px solid var(--rule);padding:9px 8px}
.item-box h2{font-family:"Special Elite",monospace;font-weight:400;font-size:18px;letter-spacing:1.5px;line-height:1}
.desc{font-size:10.4px;line-height:1.35;color:var(--ink-soft);margin-top:4px}
.label{font-family:"Kaushan Script",cursive;font-size:13.5px;margin-top:8px;line-height:1.1}
.opts{font-size:10.4px;font-weight:600;line-height:1.35}
.cols{display:flex}
.cols .col{padding-right:10px}
.cols .col+.col{border-left:1px solid var(--rule);padding-left:12px}
.pita-block{position:absolute;left:70px;top:1060px;width:350px}
.pita-block h2{font-family:"Special Elite",monospace;font-weight:400;font-size:18px;letter-spacing:1.5px}
.legend{position:absolute;left:84px;top:1168px;display:flex;gap:14px;font-size:8px;color:#eee;align-items:center}
.legend span{display:flex;align-items:center;gap:3px}
.legend i{display:inline-block;width:12px;height:12px;border-radius:50%;border:1px solid #eee}
.legend i.veg{background:var(--green);border-color:var(--green)}
.dish-photo{position:absolute;border-radius:14px}
.plate{background:radial-gradient(ellipse at 50% 50%,#c9964f 0 35%,#e8c66a 36% 52%,var(--plate) 54%)}
.steak{border-radius:6px;background:linear-gradient(90deg,#5a3a2a 0 45%,#c73a2a 55%,#4f8a3a 75%,#eee 100%)}
.pita-plate{border-radius:50%;background:radial-gradient(circle,#e0b77a 0 60%,var(--plate) 62%)}
</style>
</head>
<body>
<main class="menu-page">
  <div class="paper-panel"><div class="stitch-edge"></div></div>

  <header class="title-banner">
    <div class="sprig left" role="img" aria-label="Olive sprig ornament"></div>
    <h1>from Our Grill</h1>
    <div class="sprig right" role="img" aria-label="Olive sprig ornament"></div>
  </header>

  <section class="item-box" style="top:126px;height:134px">
    <h2>FILLETS</h2>
    <p class="desc">Grilled tender pork or chicken fillets topped with an oregano and lemon sauce. Served with fries. £ 13.00</p>
    <p class="label">Add extras:</p>
    <p class="opts">Side Salad + £ 2.50<br>Extra Haloumi + £ 3.50<br>Extra Tzatziki + £ 3.00</p>
  </section>

  <section class="item-box" style="top:273px;height:124px">
    <h2>LAMB CUTLETS</h2>
    <p class="desc">Tender lamb cutlets grilled to perfection and<br>served with fries. £ 16.00</p>
    <p class="label">Add side:</p>
    <p class="opts">Side Salad + £ 2.50</p>
  </section>

  <section class="item-box" style="top:408px;height:186px">
    <h2>VILLAGE SAUSAGES</h2>
    <p class="desc">Two large grilled sausages from Thrace served with mustard or lemon dressing. Served with fries. £ 9.50</p>
    <p class="label">Dressings:</p>
    <p class="opts">Mustard | Lemon | None</p>
    <div class="cols">
      <div class="col"><p class="label">Add extras:</p><p class="opts">Side Salad + £ 2.50<br>Extra Haloumi + £ 3.50<br>Extra Tzatziki + £ 3.00</p></div>
      <div class="col"><p class="label">Pita Bread</p><p class="opts">No Pita<br>1 x Pita<br>2 x Pita+ £ 1.00</p></div>
    </div>
  </section>

  <section class="item-box" style="top:611px;height:213px">
    <h2>SIRLOIN STEAK</h2>
    <p class="desc">350gr Juicy Sirloin Steak! One of the most premium items of our menu. Dry aged mature for 18 days, then grilled to perfection by our Head Chef! This highly desired cut of meat has a beefier flavour, less fat and medium tender, as it comes from an area where muscles get more exercise. We recommend it to be enjoyed medium cooked. £24.50</p>
    <p class="label">Preferred Cooking</p>
    <p class="opts">Rare | Medium Rare | Medium | Medium Well | Well</p>
    <div class="cols">
      <div class="col" style="width:175px"><p class="label">Choose Side:</p><p class="opts">Fries | Side Salad + £ 2.50</p></div>
      <div class="col"><p class="label">Pita Bread</p><p class="opts">No Pita<br>1 x Pita<br>2 x Pita+ £ 1.0</p></div>
    </div>
  </section>

  <section class="item-box" style="top:838px;height:208px">
    <h2>RIBEYE STEAK</h2>
    <p class="desc">350gr Juicy Rib-Eye Steak! One of the most premium items of our menu. Dry aged mature for 18 days, then grilled to perfection by our Head Chef! This highly desired cut of meat has full flavour, soft and rich texture and juicy finish. We recommend it to be enjoyed medium cooked. £ 24.50</p>
    <p class="label">Preferred Cooking</p>
    <p class="opts">Rare | Medium Rare | Medium | Medium Well | Well</p>
    <div class="cols">
      <div class="col" style="width:175px"><p class="label">Choose Side:</p><p class="opts">Fries | Side Salad + £ 2.50</p></div>
      <div class="col"><p class="label">Pita Bread</p><p class="opts">No Pita<br>1 x Pita<br>2 x Pita+ £ 1.0</p></div>
    </div>
  </section>

  <section class="pita-block">
    <h2>PITA</h2>
    <p class="desc">Greek pita resembles very much the Arabic flatbread, but unlike them, our pita breads are slightly thicker. Their taste is neutral and they soft and flexible so that it can be used as a wrap. Great addition for any mezze or appetizer. + £ 1.00</p>
  </section>

  <footer class="legend">
    <span><i></i>= gluten free</span>
    <span><i class="veg"></i>= vegetarian</span>
    <span><i class="veg"></i>= vegan</span>
  </footer>

  <div class="dish-photo plate" style="left:450px;top:120px;width:262px;height:184px" role="img" aria-label="Grilled chicken fillets with fries and lemon on a white plate"></div>
  <div class="dish-photo plate" style="left:532px;top:284px;width:245px;height:196px" role="img" aria-label="Grilled lamb cutlets with fries and lemon on a white plate"></div>
  <div class="dish-photo plate" style="left:450px;top:444px;width:262px;height:192px" role="img" aria-label="Grilled village sausages with fries and lemon on a white plate"></div>
  <div class="dish-photo steak" style="left:466px;top:632px;width:311px;height:192px" role="img" aria-label="Grilled sirloin steak with Greek salad"></div>
  <div class="dish-photo steak" style="left:450px;top:826px;width:327px;height:198px" role="img" aria-label="Grilled ribeye steak with Greek salad"></div>
  <div class="dish-photo pita-plate" style="left:518px;top:992px;width:210px;height:192px" role="img" aria-label="Plate of grilled pita bread wedges"></div>
</main>
</body>
</html>
```